Business Card Design

Just looking for a good designs that looks good with our company logo. I'd like it to be simple and to the point. Just including contact information, our logo, and my name somewhere on the card so future clients know who they're contacting, and a couple services offered. The two images I attached are pictures of our logo. I don't care which color they they are, I just attached both images to give a reference of logo colors depending on the color of the card.
Names: Derek Hallory
Phone: 816-442-7061
Email: greenvalebrush@mailzen.test
Services offered:
Mowing
Fertilization
Aeration
Bed & tree maintenance
and more.
Industry/Entity Type
Business
Contact Information for Business Card
Names: Derek Hallory
Phone: 816-442-7061
Look and feel

```html
<!DOCTYPE html>
<html lang="en">
<head>
<meta charset="utf-8">
<title>Greenvale Brush – Business Card</title>
<link href="https://fonts.googleapis.com/css2?family=Arimo:wght@400;700&display=swap" rel="stylesheet">
<style>
  :root {
    --backdrop: #5e4129;
    --card-white: #ffffff;
    --ink-navy: #2f3142;
    --accent-red: #ef5b47;
    --accent-red-light: #f3705c;
    --text-white: #ffffff;
    --text-dark: #2c2d3a;
  }
  * { box-sizing: border-box; margin: 0; padding: 0; }
  html, body {
    width: 1200px;
    height: 900px;
    overflow: hidden;
    background: var(--backdrop);
    font-family: "Arimo", Arial, sans-serif;
  }
  .canvas {
    width: 1200px;
    height: 900px;
    display: flex;
    align-items: center;
    justify-content: center;
  }
  .business-card {
    position: relative;
    width: 1000px;
    height: 572px;
    background: var(--card-white);
    overflow: hidden;
    box-shadow: 0 14px 30px rgba(0,0,0,0.35);
  }
  .brand {
    position: absolute;
    left: 70px;
    top: 110px;
    display: flex;
    align-items: center;
    gap: 18px;
  }
  .brand-dot {
    width: 58px;
    height: 58px;
    border-radius: 50%;
    background: var(--accent-red);
  }
  .brand-name {
    font-weight: 700;
    font-size: 42px;
    color: var(--ink-navy);
    letter-spacing: 1px;
    text-transform: uppercase;
  }
  .contact {
    position: absolute;
    right: 70px;
    top: 62px;
    text-align: right;
    color: var(--text-dark);
  }
  .contact-name {
    font-weight: 700;
    font-size: 40px;
    letter-spacing: -0.5px;
    color: var(--ink-navy);
    margin-bottom: 10px;
  }
  .contact-line {
    font-size: 26px;
    line-height: 1.3;
  }
  .stripe-top {
    position: absolute;
    left: 0; right: 0;
    top: 300px;
    height: 26px;
    background: var(--ink-navy);
  }
  .services-band {
    position: absolute;
    left: 0; right: 0;
    top: 326px;
    height: 196px;
    background: linear-gradient(90deg, var(--accent-red) 0%, var(--accent-red-light) 100%);
    color: var(--text-white);
  }
  .stripe-bottom {
    position: absolute;
    left: 0; right: 0;
    top: 522px;
    bottom: 0;
    background: var(--ink-navy);
  }
  .services-heading {
    position: absolute;
    left: 390px;
    top: 34px;
    font-size: 30px;
  }
  .service-list {
    list-style: none;
    position: absolute;
    font-size: 28px;
    line-height: 1.2;
  }
  .service-list li {
    display: flex;
    align-items: center;
    gap: 8px;
  }
  .service-list--left {
    left: 40px;
    bottom: 16px;
  }
  .service-list--right {
    right: 40px;
    top: 14px;
    text-align: right;
  }
  .service-list--right li { justify-content: flex-end; }
  .star { width: 24px; height: 24px; flex: none; }
</style>
</head>
<body>
<main class="canvas">
  <article class="business-card">
    <div class="brand">
      <span class="brand-dot"></span>
      <span class="brand-name">Greenvale Brush</span>
    </div>

    <div class="contact">
      <p class="contact-name">Derek Hallory</p>
      <p class="contact-line">816-442-7061</p>
      <p class="contact-line">greenvalebrush@mailzen.test</p>
    </div>

    <div class="stripe-top"></div>

    <section class="services-band">
      <h2 class="services-heading" style="font-weight:400">Services offered:</h2>

      <ul class="service-list service-list--left">
        <li><svg class="star" viewBox="0 0 24 24"><polygon fill="#fff" points="12,1 15,9 23,9 16.5,14 19,22 12,17 5,22 7.5,14 1,9 9,9"/></svg>Mowing</li>
        <li><svg class="star" viewBox="0 0 24 24"><polygon fill="#fff" points="12,1 15,9 23,9 16.5,14 19,22 12,17 5,22 7.5,14 1,9 9,9"/></svg>Aeration</li>
        <li><svg class="star" viewBox="0 0 24 24"><polygon fill="#fff" points="12,1 15,9 23,9 16.5,14 19,22 12,17 5,22 7.5,14 1,9 9,9"/></svg>Fertilization</li>
      </ul>

      <ul class="service-list service-list--right">
        <li>Bed &amp; tree<svg class="star" viewBox="0 0 24 24"><polygon fill="#fff" points="12,1 15,9 23,9 16.5,14 19,22 12,17 5,22 7.5,14 1,9 9,9"/></svg></li>
        <li>maintenance</li>
        <li>and more.<svg class="star" viewBox="0 0 24 24"><polygon fill="#fff" points="12,1 15,9 23,9 16.5,14 19,22 12,17 5,22 7.5,14 1,9 9,9"/></svg></li>
      </ul>
    </section>

    <div class="stripe-bottom"></div>
  </article>
</main>
</body>
</html>
```